Business card design needed

We would like a new design for our window furnishings & home decor business. We supply & install blinds, curtains, shutters etc. We are about to incorporate home decor products like cushoins & throws...
We'd like to use moderns browns & green tones. Casual but elegant style. Maybe textured/patterned look design. Design should communicate quality and great value with latest designs.

website & FB page & email is still to be advised so pls provide space.

Contact Information for Business Card

Marlow Haven
Window Furnishings & Home Decor
Gabrielle - Interior Stylist
Call us now for a free measure & quote - 63124098
0412 905 316
0418 276 540

```html
<!DOCTYPE html>
<html lang="en">
<head>
<meta charset="utf-8">
<title>Marlow Haven – Business Card</title>
<link href="https://fonts.googleapis.com/css2?family=Didact+Gothic&family=Questrial&display=swap" rel="stylesheet">
<style>
  :root {
    --page-bg: #ece8e2;
    --wood-dark: #1f140d;
    --wood-mid: #3a2618;
    --wood-light: #4a3120;
    --leaf: #a9c23f;
    --leaf-soft: #b7cf4c;
    --earth: #4b2f1b;
    --earth-deep: #3f2716;
    --cream: #f4efe4;
    --ink: #3a2414;
  }
  * { box-sizing: border-box; margin: 0; padding: 0; }
  html, body { width: 1200px; height: 733px; overflow: hidden; }
  body {
    background: var(--page-bg);
    font-family: "Didact Gothic", "Questrial", sans-serif;
    position: relative;
  }
  .card {
    position: absolute;
    top: 201px;
    width: 540px;
    height: 330px;
    overflow: hidden;
    box-shadow: 0 6px 18px rgba(0,0,0,0.18);
  }
  /* Front */
  .card-front { left: 40px; }
  .wood-texture {
    position: absolute; inset: 0;
    background: linear-gradient(90deg, var(--wood-dark) 0%, var(--wood-mid) 30%, var(--wood-light) 50%, var(--wood-mid) 70%, var(--wood-dark) 100%);
  }
  .brand {
    position: absolute; left: 0; right: 0; top: 118px;
    text-align: center;
  }
  .brand-name {
    font-family: "Questrial", sans-serif;
    color: var(--leaf);
    font-size: 44px;
    letter-spacing: 0.5px;
  }
  .brand-tagline {
    margin-top: 10px;
    color: var(--cream);
    font-size: 19px;
    letter-spacing: 0.3px;
  }
  /* Back */
  .card-back { left: 620px; background: var(--earth); }
  .name-band {
    position: absolute; left: 0; right: 0; top: 0; height: 136px;
    background: linear-gradient(180deg, var(--leaf-soft), var(--leaf));
    text-align: center;
    padding-top: 46px;
    color: var(--ink);
  }
  .person-name { font-family: "Questrial", sans-serif; font-size: 34px; line-height: 1; }
  .person-role { font-size: 15px; margin-top: 4px; }
  .contact-area {
    position: absolute; left: 0; right: 0; top: 136px; bottom: 0;
    background: linear-gradient(180deg, var(--earth), var(--earth-deep));
    color: var(--cream);
  }
  .call-line {
    position: absolute; top: 26px; left: 0; right: 0;
    text-align: center; font-size: 17px;
  }
  .email-label {
    position: absolute; top: 78px; right: 296px;
    display: flex; align-items: center; gap: 8px;
    font-size: 15px; color: var(--leaf);
  }
  .divider {
    position: absolute; left: 270px; top: 72px; width: 1px; height: 100px;
    background: var(--cream); opacity: 0.7;
  }
  .phone-list {
    position: absolute; left: 284px; top: 72px;
    font-size: 16px; line-height: 24px;
  }
  .phone-row { display: flex; align-items: center; gap: 10px; }
  .phone-row .icon { width: 14px; height: 14px; }
  .phone-row.no-icon { padding-left: 24px; }
  .web-address {
    position: absolute; left: 30px; bottom: 20px;
    color: var(--leaf); font-size: 15px;
  }
</style>
</head>
<body>
  <section class="card card-front">
    <div class="wood-texture" role="img" aria-label="Dark brown vertical wood-grain texture"></div>
    <div class="brand">
      <div class="brand-name">Marlow Haven</div>
      <div class="brand-tagline">Window Furnishings &amp; Home Decor</div>
    </div>
  </section>

  <section class="card card-back">
    <div class="name-band">
      <div class="person-name">Gabrielle</div>
      <div class="person-role">Interior Stylist</div>
    </div>
    <div class="contact-area">
      <p class="call-line">Call us now for a free measure &amp; quote</p>
      <div class="email-label">Email
        <svg width="16" height="12" viewBox="0 0 16 12" aria-hidden="true">
          <rect x="0.75" y="0.75" width="14.5" height="10.5" rx="1.5" fill="none" stroke="#f4efe4" stroke-width="1.5"/>
          <path d="M1 1.5 L8 7 L15 1.5" fill="none" stroke="#f4efe4" stroke-width="1.5"/>
        </svg>
      </div>
      <div class="divider"></div>
      <div class="phone-list">
        <div class="phone-row">
          <svg class="icon" viewBox="0 0 14 14" aria-hidden="true">
            <path d="M3 1 L5 1 L6 4 L4.5 5 C5.3 7 7 8.7 9 9.5 L10 8 L13 9 L13 11 C13 12 12 13 11 13 C5.5 12.5 1.5 8.5 1 3 C1 2 2 1 3 1 Z" fill="#f4efe4"/>
          </svg>
          <span>63124098</span>
        </div>
        <div class="phone-row">
          <svg class="icon" viewBox="0 0 14 14" aria-hidden="true">
            <rect x="3.5" y="0.5" width="7" height="13" rx="1.5" fill="none" stroke="#f4efe4" stroke-width="1.2"/>
            <rect x="5" y="2.5" width="4" height="6.5" fill="#f4efe4"/>
            <circle cx="7" cy="11.3" r="0.9" fill="#f4efe4"/>
          </svg>
          <span>0412 905 316</span>
        </div>
        <div class="phone-row no-icon"><span>0418 276 540</span></div>
      </div>
      <div class="web-address">www.SiteAddress.com</div>
    </div>
  </section>
</body>
</html>
```